Southern Rigline Academy needs a modern website that oozes professionalism

Our current website is boring and looks like everyone elses. We need a modern website that says we are the best at plant operator training. We use Varnhold and Delvaro equipment for our training. We train all over Australia in Civil Construction, Mining and Quarrying. We want to be the "Go to" website for all plant operator training in Australia.

Industry/Entity Type

Heavy Machinery Training

Colors
0054AA
0677BA
7BADD7
CADEEF
E8F1F8
FFF300
FFF600
FEFA6F
FFFEC7
FFFEE8

```html
<!DOCTYPE html>
<html lang="en">
<head>
<meta charset="utf-8">
<title>Southern Rigline Academy — Plant Operator Training</title>
<link href="https://fonts.googleapis.com/css2?family=Poppins:wght@400;500;600;700;800&display=swap" rel="stylesheet">
<style>
:root{
  --navy:#12325e;
  --navy-deep:#0b2344;
  --blue:#0054AA;
  --blue-mid:#0677BA;
  --blue-soft:#7BADD7;
  --blue-pale:#E8F1F8;
  --yellow:#F7C60C;
  --yellow-soft:#FEFA6F;
  --ink:#1c2533;
  --grey:#5d6673;
  --line:#dfe5ec;
  --white:#ffffff;
}
*{box-sizing:border-box;margin:0;padding:0}
html,body{width:1200px;height:4852px;overflow:hidden}
body{font-family:'Poppins',sans-serif;color:var(--ink);background:var(--white);position:relative}
.btn{display:inline-flex;align-items:center;justify-content:center;border-radius:40px;font-weight:700;text-transform:uppercase;letter-spacing:.5px;text-decoration:none}
.btn-yellow{background:var(--yellow);color:var(--navy-deep)}
.btn-navy{background:var(--navy);color:var(--white)}

/* header */
.topbar{height:100px;display:flex;align-items:center;justify-content:space-between;padding:0 72px 0 80px}
.brand{display:flex;align-items:center;gap:12px}
.brand-dot{width:34px;height:34px;border-radius:50%;background:var(--yellow)}
.brand-name{font-weight:800;font-size:17px;line-height:1.1;color:var(--navy);text-transform:uppercase;width:150px}
.top-actions{display:flex;gap:8px}
.top-actions .btn{height:34px;font-size:12px;padding:0 22px}
.mainnav{height:44px;background:var(--navy);display:flex;align-items:stretch;padding-left:80px}
.mainnav a{display:flex;align-items:center;padding:0 18px;color:var(--white);font-size:11.5px;font-weight:600;text-decoration:none;text-transform:uppercase}
.mainnav a.active{background:var(--yellow);color:var(--navy-deep)}

/* hero */
.hero{height:696px;position:relative;background:linear-gradient(100deg,#1d2a3c 0%,#3b4b5e 35%,#a7875a 65%,#e2a552 85%,#f1c27a 100%);overflow:hidden}
.hero-photo{position:absolute;inset:0;background:radial-gradient(ellipse at 72% 60%,rgba(36,30,20,.75) 0%,rgba(36,30,20,0) 45%),linear-gradient(180deg,rgba(0,0,0,0) 70%,rgba(40,30,15,.6) 100%)}
.hero-copy{position:absolute;left:80px;top:150px}
.hero h1{color:var(--white);font-size:56px;font-weight:800;line-height:1.14;text-transform:uppercase;width:620px}
.hero .btn{margin-top:44px;height:58px;width:276px;font-size:16px}
.dots{position:absolute;left:50%;bottom:70px;transform:translateX(-50%);display:flex;gap:8px}
.dots span{width:10px;height:10px;border-radius:50%;background:rgba(255,255,255,.55)}
.dots span.on{background:var(--white)}

/* course cards */
.courses{height:480px;padding:60px 80px 0;display:flex;gap:37px;background:var(--white)}
.course-card{width:232px;height:318px;background:var(--white);box-shadow:0 4px 18px rgba(16,40,80,.12);text-align:center}
.course-card .photo{height:150px}
.course-card h3{font-size:14.5px;font-weight:700;color:var(--navy);text-transform:uppercase;margin-top:18px}
.course-card p{font-size:11.5px;color:var(--grey);line-height:1.5;margin-top:6px;height:36px}
.course-card .btn{margin-top:14px;height:24px;font-size:9.5px;padding:0 18px}

/* section titles */
.section-title{text-align:center;font-weight:800;font-size:40px;text-transform:uppercase;color:var(--ink)}
.section-title::before{content:"";display:block;width:110px;height:3px;background:var(--navy);margin:0 auto 18px}

/* online training */
.online{height:1032px;padding-top:0}
.online .section-title{margin-top:0}
.module{position:absolute;left:0;width:1200px;height:240px}
.module .photo{position:absolute;top:0;width:412px;height:240px}
.module .copy{position:absolute;top:18px;width:440px}
.module h3{font-size:25px;font-weight:700;color:var(--navy);text-transform:uppercase;line-height:1.2}
.module p{font-size:13px;color:var(--grey);line-height:1.6;margin-top:22px}
.module .btn{margin-top:22px;height:38px;width:150px;font-size:11px}

/* services */
.services{position:absolute;top:2392px;left:0;width:1200px;height:848px;background:linear-gradient(180deg,#0b2344 0%,#1b3c66 45%,#4a627e 100%)}
.services .section-title{color:var(--white);margin-top:92px}
.services .section-title::before{background:var(--yellow)}
.service-row{position:absolute;top:208px;left:80px;display:flex;gap:25px}
.service-card{width:330px;height:440px;background:var(--white);text-align:center}
.service-card .photo{height:200px}
.service-card h3{font-size:20px;font-weight:700;text-transform:uppercase;color:var(--ink);line-height:1.2;margin:28px 20px 0}
.service-card p{font-size:12.5px;color:var(--grey);line-height:1.6;margin:14px 28px 0}
.services .view-more{position:absolute;left:50%;top:720px;transform:translateX(-50%);height:56px;width:176px;font-size:15px}

/* why */
.why{position:absolute;top:3240px;left:0;width:1200px;height:580px;background:var(--white)}
.why .section-title{margin-top:60px}
.why .intro{width:860px;margin:26px auto 0;text-align:center;font-size:13px;color:var(--grey);line-height:1.7}
.why-row{position:absolute;top:250px;left:170px;display:flex;gap:80px}
.why-item{width:233px;text-align:center}
.why-item .badge{width:148px;height:148px;border-radius:50%;margin:0 auto;display:flex;align-items:center;justify-content:center;background:var(--navy);border:8px solid var(--blue-pale)}
.why-item .badge.gold{background:var(--yellow)}
.why-item h4{font-size:17px;font-weight:700;text-transform:uppercase;margin-top:26px}
.why-item p{font-size:12.5px;color:var(--grey);line-height:1.5;margin-top:8px}

/* giveaway */
.giveaway{position:absolute;top:3820px;left:0;width:1200px;height:440px;background:linear-gradient(100deg,#0b2344 0%,#1f3d64 40%,#7a6a56 68%,#e5a248 85%,#f6c97c 100%)}
.giveaway h2{position:absolute;left:80px;top:56px;width:620px;color:var(--white);font-size:48px;font-weight:800;line-height:1.18;text-transform:uppercase}
.giveaway .btn{position:absolute;left:80px;top:300px;height:58px;width:276px;font-size:16px}

/* footer */
.footer{position:absolute;top:4260px;left:0;width:1200px;height:540px;background:var(--white)}
.footer .brand{position:absolute;left:50%;top:54px;transform:translateX(-50%)}
.footer .brand-name{width:auto;font-size:22px}
.footer .brand-dot{width:44px;height:44px}
.footer-cols{position:absolute;top:180px;left:190px;display:flex;gap:0}
.footer-col{width:230px}
.footer-col h5{font-size:13px;font-weight:700;text-transform:uppercase;color:var(--ink)}
.footer-col h5::after{content:"";display:block;width:34px;height:2px;background:var(--yellow);margin-top:8px}
.footer-col ul{list-style:none;margin-top:16px}
.footer-col li{font-size:12px;color:var(--grey);line-height:2}
.footer-col li.gap{margin-top:14px}
.contact li{display:flex;align-items:center;gap:12px;margin-bottom:14px;line-height:1.4}
.contact .ico{width:30px;height:30px;border-radius:50%;background:var(--navy);flex:none;display:flex;align-items:center;justify-content:center}
.bottombar{position:absolute;top:4800px;left:0;width:1200px;height:52px;background:var(--navy);display:flex;align-items:center;justify-content:space-between;padding:0 80px}
.bottombar p{color:#c8d6e6;font-size:11px}
.socials{display:flex;gap:8px}
.socials span{width:24px;height:24px;border-radius:50%;border:1.5px solid #c8d6e6}
</style>
</head>
<body>

<header>
  <div class="topbar">
    <div class="brand"><span class="brand-dot"></span><span class="brand-name">Southern Rigline Academy</span></div>
    <div class="top-actions">
      <a class="btn btn-yellow" href="#">Course Calendar</a>
      <a class="btn btn-navy" href="#">Student Handbook</a>
    </div>
  </div>
  <nav class="mainnav">
    <a class="active" href="#">Home</a>
    <a href="#">About</a>
    <a href="#">Courses Onsite / Private Courses</a>
    <a href="#">Online Training</a>
    <a href="#">Our Services</a>
    <a href="#">Student Information</a>
    <a href="#">Contact</a>
  </nav>
</header>

<section class="hero">
  <div class="hero-photo" role="img" aria-label="Backhoe loader working on a construction site at sunset"></div>
  <div class="hero-copy">
    <h1>Training and experience you can rely on</h1>
    <a class="btn btn-yellow" href="#">Contact us now</a>
  </div>
  <div class="dots"><span class="on"></span><span></span><span></span></div>
</section>

<section class="courses">
  <article class="course-card">
    <div class="photo" role="img" aria-label="Worker in hard hat and safety vest" style="background:linear-gradient(135deg,#c9b79a,#e0a944 60%,#6a7b8f)"></div>
    <h3>Safety Training</h3>
    <p>White Card<br>First Aid / CPR</p>
    <a class="btn btn-yellow" href="#">Read more</a>
  </article>
  <article class="course-card">
    <div class="photo" role="img" aria-label="Coal mining operation" style="background:linear-gradient(135deg,#6b6257,#3c3833 60%,#8f8472)"></div>
    <h3>Coal Mine Training</h3>
    <p>Standard 11<br>Supervisor S123</p>
    <a class="btn btn-yellow" href="#">Read more</a>
  </article>
  <article class="course-card">
    <div class="photo" role="img" aria-label="Yellow haul truck on a mine site" style="background:linear-gradient(135deg,#9db0c4,#d9b44a 55%,#7a6c55)"></div>
    <h3>Plant Operator Training</h3>
    <p>Haul Truck</p>
    <a class="btn btn-yellow" href="#">Read more</a>
  </article>
  <article class="course-card">
    <div class="photo" role="img" aria-label="Operator on an elevated work platform" style="background:linear-gradient(135deg,#a9c3da,#e48a3a 55%,#5c6d80)"></div>
    <h3>High Risk Licences</h3>
    <p>LF – Forklift<br>WP – Elevated Work Platform</p>
    <a class="btn btn-yellow" href="#">Read more</a>
  </article>
</section>

<section class="online">
  <h2 class="section-title">Online Training</h2>

  <div class="module" style="top:1460px">
    <div class="photo" role="img" aria-label="Red isolation switch on industrial plant" style="left:148px;background:linear-gradient(135deg,#8fa2b5,#c23a2f 45%,#d9a425 75%,#55616d)"></div>
    <div class="copy" style="left:600px">
      <h3>Isolate and access plant</h3>
      <p>*It is a condition of enrolment that you supply a valid unique student identifier (USI). If you don't already have a USI, you can apply for one online at www.studentid.example</p>
      <a class="btn btn-yellow" href="#">Enroll now</a>
    </div>
  </div>

  <div class="module" style="top:1760px">
    <div class="copy" style="left:160px">
      <h3>Operate small plant &amp; equipment</h3>
      <p>*It is a condition of enrolment that you supply a valid unique student identifier (USI). If you don't already have a USI, you can apply for one online at www.studentid.example</p>
      <a class="btn btn-yellow" href="#">Enroll now</a>
    </div>
    <div class="photo" role="img" aria-label="Worker cutting concrete with a handheld saw" style="left:640px;background:linear-gradient(135deg,#d7dbe0,#b9c0c7 50%,#8bbf3a 80%,#6d747c)"></div>
  </div>

  <div class="module" style="top:2060px">
    <div class="photo" role="img" aria-label="Vehicles and equipment lined up in a workshop" style="left:148px;background:linear-gradient(135deg,#e1e4e8,#b7bec6 50%,#d8b236 75%,#7a828b)"></div>
    <div class="copy" style="left:600px">
      <h3>Test operational function of vehicles &amp; equipment</h3>
      <p>*It is a condition of enrolment that you supply a valid unique student identifier (USI). If you don't already have a USI, you can apply for one online at www.studentid.example</p>
      <a class="btn btn-yellow" href="#">Enroll now</a>
    </div>
  </div>
</section>

<section class="services" role="img" aria-label="Mining haul trucks on a site behind a dark blue overlay">
  <h2 class="section-title">Our Services</h2>
  <div class="service-row">
    <article class="service-card">
      <div class="photo" role="img" aria-label="Large mining haul truck" style="background:linear-gradient(135deg,#b6c2cd,#d7a934 55%,#6f5f48)"></div>
      <h3>Credit Transfers</h3>
      <p>Southern Rigline Academy acknowledges the requirement as a Registered Training Organisation to recognise the awards issued by other RTOs. This is limited to outcomes that are drawn from the national skills framework being units of competency.</p>
    </article>
    <article class="service-card">
      <div class="photo" role="img" aria-label="Yellow wheel loader on a work site" style="background:linear-gradient(135deg,#c4ccd4,#dcb23e 55%,#7d705c)"></div>
      <h3>Verification of Competency</h3>
      <p>A number of Office of the Federal Safety Commissioner criteria reference the requirement to ensure that a 'competent person' undertakes a particular task or activity, as identified in the OFSC Evidence Guide.</p>
    </article>
    <article class="service-card">
      <div class="photo" role="img" aria-label="White disposable respirator mask" style="background:linear-gradient(135deg,#f1f2f3,#d8dadc 60%,#b0b5ba)"></div>
      <h3>Respirator Fit Testing</h3>
      <p>Respirator Fit testing, commonly known as a mask fit test or facial fit test, is a way to determine if an adequate seal is achieved on the wearer of their chosen respiratory protective device (RPD).</p>
    </article>
  </div>
  <a class="btn btn-yellow view-more" href="#">View more</a>
</section>

<section class="why">
  <h2 class="section-title">Why choose us?</h2>
  <p class="intro">Southern Rigline Academy consultants have come from the same industries that we cover back to. Our wealth of first hand knowledge and experience enables us to make invaluable contributions to all facets of safety and training in your workplace.</p>
  <div class="why-row">
    <div class="why-item">
      <div class="badge">
        <svg width="58" height="58" viewBox="0 0 58 58" fill="none" stroke="#fff" stroke-width="3" stroke-linecap="round" stroke-linejoin="round"><rect x="12" y="8" width="34" height="42" rx="3"/><path d="M20 22h18M20 30h18M20 38h10"/></svg>
      </div>
      <h4>We are passionate</h4>
      <p>We are passionate about health and Safety</p>
    </div>
    <div class="why-item">
      <div class="badge gold">
        <svg width="58" height="58" viewBox="0 0 58 58" fill="none" stroke="#12325e" stroke-width="3" stroke-linecap="round" stroke-linejoin="round"><path d="M8 30l10-10 8 4 6-4 18 12-10 10-6-4-4 4-8-6z"/><path d="M26 24l8 8"/></svg>
      </div>
      <h4>We are dependable</h4>
      <p>Let us deliver the right training solution for your business</p>
    </div>
    <div class="why-item">
      <div class="badge">
        <svg width="58" height="58" viewBox="0 0 58 58" fill="none" stroke="#fff" stroke-width="3" stroke-linecap="round" stroke-linejoin="round"><circle cx="29" cy="24" r="14"/><path d="M21 36l-4 16 12-6 12 6-4-16"/><path d="M23 24l4 4 8-8"/></svg>
      </div>
      <h4>Nationally recognised</h4>
      <p>We are accredited to deliver nationally recognised training</p>
    </div>
  </div>
</section>

<section class="giveaway" role="img" aria-label="Excavator silhouetted against a sunset sky">
  <h2>Give away – Thunderline or a boat package worth $35,000</h2>
  <a class="btn btn-yellow" href="#">Contact us now</a>
</section>

<footer class="footer">
  <div class="brand"><span class="brand-dot"></span><span class="brand-name">Southern Rigline Academy</span></div>
  <div class="footer-cols">
    <div class="footer-col">
      <h5>Working hours</h5>
      <ul>
        <li>Monday to Friday</li>
        <li>7:30 AM – 4:30 PM</li>
        <li class="gap">Saturday &amp; Sunday:</li>
        <li>Holiday</li>
      </ul>
    </div>
    <div class="footer-col">
      <h5>Courses</h5>
      <ul>
        <li>» Full Qualifications</li>
        <li>» High Risk Licencing</li>
        <li>» Plant Operator Tickets</li>
        <li>» Short Courses</li>
      </ul>
    </div>
    <div class="footer-col">
      <h5>Student resources</h5>
      <ul>
        <li>» Enrolment Form</li>
        <li>» Student Handbook</li>
        <li>» Support</li>
        <li>» Contact us</li>
      </ul>
    </div>
    <div class="footer-col contact">
      <h5>Contact details</h5>
      <ul>
        <li><span class="ico"><svg width="14" height="14" viewBox="0 0 14 14" fill="#fff"><path d="M7 1a4 4 0 0 0-4 4c0 3 4 8 4 8s4-5 4-8a4 4 0 0 0-4-4zm0 5.5A1.5 1.5 0 1 1 7 3.5a1.5 1.5 0 0 1 0 3z"/></svg></span>18 Calder Lane, Kestrel<br>QLD 4999</li>
        <li><span class="ico"><svg width="14" height="14" viewBox="0 0 14 14" fill="#fff"><path d="M3 1l2.5 0 1 3-1.5 1.2a7 7 0 0 0 3.8 3.8L10 7.5l3 1V11a1.5 1.5 0 0 1-1.5 1.5A10.5 10.5 0 0 1 1.5 2.5 1.5 1.5 0 0 1 3 1z"/></svg></span>1300 000 482</li>
        <li><span class="ico"><svg width="14" height="14" viewBox="0 0 14 14" fill="none" stroke="#fff" stroke-width="1.4"><rect x="1.5" y="3" width="11" height="8" rx="1"/><path d="M1.5 3.5L7 8l5.5-4.5"/></svg></span>training@sracademy.example</li>
      </ul>
    </div>
  </div>
</footer>

<div class="bottombar">
  <p>© Southern Rigline Academy – RTO number #48217</p>
  <div class="socials"><span></span><span></span><span></span><span></span></div>
</div>

</body>
</html>
```